Simple elegant business card

General card for a fin and television director.
Just want name, email, phone and address.

Target Market(s)

Prospective employers

Industry/Entity Type

Business

Requirements
Must have
• As above
Nice to have
• Logo but not necessary.
Should not have
• Not too colourful or funky.
• Simplicity and elegance the way to go.

```html
<!DOCTYPE html>
<html lang="en">
<head>
<meta charset="utf-8">
<title>Nora Hale — Business Card</title>
<link rel="stylesheet" href="https://fonts.googleapis.com/css2?family=Zilla+Slab:wght@300&family=Fira+Sans:wght@300&display=swap">
<style>
  :root {
    --page-bg: #ececec;
    --card-bg: #cbe6ed;
    --card-glow: #d3edf3;
    --ink: #2f3133;
  }
  html, body {
    margin: 0;
    width: 1200px;
    height: 900px;
    overflow: hidden;
    background: var(--page-bg);
  }
  .canvas {
    position: relative;
    width: 1200px;
    height: 900px;
  }
  .card {
    position: absolute;
    left: 50px;
    top: 130px;
    width: 1100px;
    height: 640px;
    background: radial-gradient(ellipse at 45% 45%, var(--card-glow), var(--card-bg) 75%);
    color: var(--ink);
  }
  .card__square {
    position: absolute;
    left: 150px;
    top: 130px;
    width: 160px;
    height: 160px;
    background: var(--ink);
  }
  .card__name {
    position: absolute;
    left: 345px;
    top: 88px;
    margin: 0;
    font-family: "Zilla Slab", Georgia, serif;
    font-weight: 300;
    font-size: 118px;
    line-height: 110px;
    letter-spacing: -1px;
  }
  .card__name span { display: block; }
  .card__contact {
    position: absolute;
    right: 60px;
    top: 472px;
    margin: 0;
    text-align: right;
    font-family: "Fira Sans", Arial, sans-serif;
    font-weight: 300;
    font-size: 36px;
    line-height: 46px;
    font-style: normal;
    letter-spacing: 0.5px;
  }
  .card__contact span { display: block; }
</style>
</head>
<body>
  <main class="canvas">
    <section class="card">
      <div class="card__square" aria-hidden="true"></div>
      <h1 class="card__name"><span>Nora</span><span>Hale</span></h1>
      <address class="card__contact">
        <span class="card__email">norahale@mail.com</span>
        <span class="card__phone">+1 310 555 0142</span>
      </address>
    </section>
  </main>
</body>
</html>
```